New Stationery New Logo for KT Mouldings Limited

We have a new logo and now want new stationary to go with it

This will be

Letterhead
Compliments Slip
Business Cards

Company details are
KT Mouldings Limited
Brindle Row, Rugby, Warwickshire, CV34 7HX, UK
Telephone : +44(0)1788 930467
Fax: +44(0)1788 918723
Email: sales@ktmouldings.example
Web: www.ktmouldings.example

Target Market(s)

Engineering / Metal Stamping

Industry/Entity Type

Manufacture

Contact Information for Business Card

Neil Garbutt
Business Development Manager
KT Mouldings Limited
Brindle Row
Rugby
Warwickshire
CV34 7HX, UK

T: +44(0)1788 930467
F: +44(0)1788 918723
E: sales@ktmouldings.example
W: www.ktmouldings.example

Font styles to use
Sans Serif

Colors
33a6d7
0555a3
3176b5
85cae6
85acd3

Requirements
Must have
• Logo

```html
<!DOCTYPE html>
<html lang="en">
<head>
<meta charset="utf-8">
<title>KT Mouldings – Business Card</title>
<link rel="stylesheet" href="https://fonts.googleapis.com/css2?family=Arimo:wght@400;700&display=swap">
<style>
  :root {
    --backdrop: #e6e6e8;
    --card: #1d1e20;
    --card-front: #151618;
    --brand-blue: #0555a3;
    --accent-blue: #3176b5;
    --text-light: #e8e8e8;
    --text-muted: #9a9a9c;
    --divider: #55575a;
  }
  * { box-sizing: border-box; margin: 0; padding: 0; }
  html, body {
    width: 1200px; height: 787px; overflow: hidden;
    background: var(--backdrop);
    font-family: "Arimo", Arial, sans-serif;
  }
  .canvas {
    position: relative; width: 1200px; height: 787px;
    display: flex; align-items: center; justify-content: center; gap: 50px;
  }
  .card {
    width: 525px; height: 300px; border-radius: 3px;
    box-shadow: 0 8px 22px rgba(0,0,0,.25);
    position: relative; overflow: hidden;
  }
  .card--front {
    background: var(--card-front);
    display: flex; flex-direction: column; align-items: center; justify-content: center; gap: 22px;
  }
  .card--front .wordmark { color: var(--text-muted); font-size: 30px; }
  .card--front .web { color: var(--text-muted); font-size: 14px; letter-spacing: 5px; }
  .wordmark {
    font-weight: 400; letter-spacing: 8px; text-transform: uppercase;
    display: flex; align-items: center; gap: 12px;
  }
  .wordmark .mark-dot {
    width: 12px; height: 12px; border-radius: 50%; background: currentColor;
  }
  .card--back { background: var(--card); display: flex; }
  .brand-side {
    width: 270px; display: flex; align-items: center; justify-content: center;
  }
  .brand-side .wordmark { color: var(--accent-blue); font-size: 20px; letter-spacing: 5px; gap: 9px; }
  .brand-side .mark-dot { width: 9px; height: 9px; }
  .divider { width: 1px; background: var(--divider); margin: 30px 0; }
  .contact-side {
    flex: 1; padding: 30px 0 0 26px; color: var(--text-light);
  }
  .person-name { color: var(--brand-blue); font-size: 19px; font-weight: 700; }
  .person-title { font-size: 15px; margin-top: 2px; }
  .address { font-size: 12.5px; line-height: 1.3; margin-top: 16px; }
  .contact-list { list-style: none; margin-top: 14px; font-size: 13px; }
  .contact-list li { display: flex; align-items: center; gap: 8px; line-height: 1.55; }
  .contact-list svg { width: 13px; height: 13px; fill: var(--brand-blue); flex: none; }
</style>
</head>
<body>
<main class="canvas">
  <section class="card card--front" aria-label="Business card front">
    <div class="wordmark"><span>KT Mouldings</span><span class="mark-dot"></span></div>
    <p class="web">www.ktmouldings.example</p>
  </section>

  <section class="card card--back" aria-label="Business card back">
    <div class="brand-side">
      <div class="wordmark"><span>KT Mouldings</span><span class="mark-dot"></span></div>
    </div>
    <div class="divider"></div>
    <div class="contact-side">
      <h1 class="person-name">Neil Garbutt</h1>
      <p class="person-title">President</p>
      <address class="address" style="font-style:normal">
        KT Mouldings Limited<br>
        Brindle Row, Rugby<br>
        Warwickshire, CV34 7HX, UK
      </address>
      <ul class="contact-list">
        <li>
          <svg viewBox="0 0 16 16" aria-hidden="true"><path d="M3 1h3l1.5 4-2 1.2a9 9 0 0 0 4.3 4.3L11 8.5l4 1.5v3a2 2 0 0 1-2 2A13 13 0 0 1 1 3a2 2 0 0 1 2-2z"/></svg>
          +44(0)1788 930467
        </li>
        <li>
          <svg viewBox="0 0 16 16" aria-hidden="true"><path d="M4 1h7v4H4zM1 6h14v7h-3v2H4v-2H1zm4 5v2h6v-2z"/></svg>
          +44(0)1788 918723
        </li>
        <li>
          <svg viewBox="0 0 16 16" aria-hidden="true"><path d="M1 3h14v1L8 9 1 4zm0 3 7 5 7-5v7H1z"/></svg>
          sales@ktmouldings.example
        </li>
        <li>
          <svg viewBox="0 0 16 16" aria-hidden="true"><circle cx="8" cy="8" r="7"/></svg>
          www.ktmouldings.example
        </li>
      </ul>
    </div>
  </section>
</main>
</body>
</html>
```